Home Based Business Website Design

Need 1 template web design. Require clean friendly website design that helps promote a Hearthside Ventures business opportunity based around personal development. The site should lean towards appealing to the female market (see target market) and be straight forward, fresh colours and good use of white space. The site should have a family focus using imagery of happy families and reinforcing the quality of life and freedom available. The site should be in a two or three column format, navigation can be top or left, there will be 6 menu items in total (E.g. home, about, testimonials, contact, faq, why me?). There should be space for a video, text, images and a clear "call to action" (contact us). The site should come across as professiona, positive, friendly and trustworthy. Scope for many more sites of this nature in the future.

Target Market(s)

People that are ready for change. People wanting to make money from a business at home. 25+ years old, mum's , professional. People that are tired of the commute and want a better quality of life. While the site should lean towards focusing on stay at home mums or working mums looking for a better life it should also be able to appeal to a wider audience (male and female) so should not be too "girly"!

Industry/Entity Type

Business

Requirements
Must have
• Fairly open to interpretation, site must have at least two columns, clear call to action, space for a video, text and images, navigation (single level 6 items).
Nice to have
• Possibly animated banner of images?
Should not have
• Try to use less obvious imagery no stressed out executives or people jumping for joy. no dark designs no purple or flouro colours. Site should be modern in design.

```html
<!DOCTYPE html>
<html lang="en">
<head>
<meta charset="utf-8">
<title>Hearthside Ventures – Improve your life</title>
<link rel="stylesheet" href="https://fonts.googleapis.com/css2?family=PT+Sans:ital,wght@0,400;0,700;1,400&display=swap">
<style>
:root{
  --navy:#3a3a7a;
  --navy-dark:#2e2e66;
  --text:#1b2b5e;
  --lilac:#8a8ae8;
  --lilac-soft:#c9c9ef;
  --periwinkle:#9a9aff;
  --salmon:#d97b7b;
  --page-top:#ffffff;
  --page-bottom:#ececf8;
  --white:#ffffff;
}
*{margin:0;padding:0;box-sizing:border-box}
html,body{width:1080px;height:1200px;overflow:hidden}
body{font-family:"PT Sans",Tahoma,sans-serif;color:var(--text);
  background:linear-gradient(180deg,var(--page-top) 0%,var(--page-bottom) 100%);position:relative}
.site{position:relative;width:1080px;height:1200px}
.brand{position:absolute;left:38px;top:62px;display:flex;align-items:center;gap:12px}
.brand-mark{width:34px;height:34px;background:var(--navy);border-radius:50%}
.brand-name{font-size:42px;font-weight:700;color:var(--navy);line-height:1;letter-spacing:-0.5px}
.header-photo{position:absolute;left:498px;top:0;width:562px;height:214px;
  background:linear-gradient(90deg,#f4f4fb 0%,#e6e6ea 45%,#dcdcdf 100%)}
.main-nav{position:absolute;left:5px;top:214px;width:1070px;height:43px;border-radius:4px;
  background:linear-gradient(180deg,#6e6ec0 0%,var(--navy-dark) 100%);display:flex;align-items:center;padding-left:22px}
.main-nav a{color:var(--white);text-decoration:none;font-weight:700;font-size:22px;padding:0 19px;
  border-right:1px solid rgba(255,255,255,.35);line-height:43px}
.main-nav a:last-child{border-right:none}
.section-title{position:absolute;font-size:19px;font-weight:700;color:var(--lilac)}
.copy{position:absolute;font-size:15px;line-height:25px;color:var(--text)}
.copy p+p{margin-top:25px}
.call-box{position:absolute;left:37px;top:661px;width:455px;height:91px;background:var(--periwinkle);
  color:var(--white);padding:10px 26px}
.call-box .call-label{font-size:18px;font-weight:700}
.call-box .call-number{font-size:38px;font-weight:700;line-height:1.05}
.call-box .call-sub{font-size:21px;line-height:1.1;display:block}
.promo-photo{position:absolute;left:41px;top:781px;width:453px;height:341px;
  background:linear-gradient(160deg,#f2f2f4 0%,#e7dcd4 50%,#d9d9de 100%)}
.promo-link{position:absolute;right:20px;top:0;text-align:right;font-size:21px;font-weight:700;
  color:var(--lilac);line-height:27px}
.promo-link a{color:var(--lilac)}
.register{position:absolute;left:583px;top:278px;width:453px;height:92px;background:var(--salmon);
  color:var(--white);font-size:30px;line-height:38px;padding:7px 14px}
.register a{color:var(--white);font-weight:700}
.video-panel{position:absolute;left:583px;top:390px;width:451px;height:277px;background:var(--lilac-soft);padding:8px 12px}
.video-panel .video-label{font-size:21px;color:#111}
.video-frame{position:absolute;left:81px;top:40px;width:304px;height:207px;
  background:linear-gradient(135deg,#5f7a3a 0%,#c8a080 45%,#7ea64a 100%)}
.video-frame svg{position:absolute;left:112px;top:64px}
.quote-box{position:absolute;left:576px;top:930px;width:204px;height:116px;
  background:linear-gradient(180deg,#ffffff 0%,var(--lilac-soft) 100%);text-align:center;padding-top:0}
.quote-box q{display:block;font-style:italic;font-size:21px;line-height:24px;color:var(--lilac)}
.quote-box a{display:block;margin-top:8px;font-size:17px;font-weight:700;color:var(--lilac);text-decoration:none;line-height:21px}
.family-photo{position:absolute;left:780px;top:936px;width:276px;height:186px;
  background:radial-gradient(ellipse at 50% 60%,#e9d4c6 0%,#f6f0ec 55%,#ffffff 100%)}
.site-footer{position:absolute;left:5px;top:1123px;width:1070px;height:43px;border-radius:4px;
  background:linear-gradient(180deg,#6e6ec0 0%,var(--navy-dark) 100%);display:flex;justify-content:center;align-items:center;gap:20px;padding-left:40px}
.site-footer a{color:var(--white);text-decoration:none;font-size:16px}
.copyright{position:absolute;right:24px;top:1176px;font-size:15px;color:var(--lilac)}
</style>
</head>
<body>
<div class="site">
  <header>
    <div class="brand"><span class="brand-mark"></span><span class="brand-name">Hearthside Ventures</span></div>
    <div class="header-photo" role="img" aria-label="Photo of a smiling woman lying on a white sofa using a laptop"></div>
    <nav class="main-nav">
      <a href="#">Home</a><a href="#">About us</a><a href="#">Testimonials</a><a href="#">Contact</a><a href="#">Faq</a><a href="#">Why me?</a>
    </nav>
  </header>

  <main>
    <h2 class="section-title" style="left:42px;top:280px">Lorem ipsum dolor sit amet</h2>
    <div class="copy" style="left:42px;top:322px;width:470px">
      <p>Consectetur adipiscing elit. Nullam fringilla lobortis velit at porttitor. Duis iaculis felis et nisi facilisis at ultricies diam pellentesque. Nunc id nibh metus. Quisque at est vestibulum ante pulvinar hendrerit eget in sapien. Nunc vel lobortis erat. Nunc non sem mi. Sed auctor dolor sit amet quam porta ut congue elit imperdiet.</p>
      <p>Duis varius interdum nulla eget facilisis. Integer sollicitudin metus in eros malesuada nec dapibus nunc tincidunt. Phasellus in mauris sed turpis ultricies accumsan. Duis ac risus risus, vel interdum leo. Suspendisse ultricies convallis ante a hendrerit. Sed libero turpis, volutpat quis condimentum eu, bibendum ac quam. Nulla nec nibh et erat commodo elementum quis a nisi. Sed consectetur arcu</p>
    </div>

    <div class="call-box">
      <span class="call-label">Call us on:</span> <span class="call-number">0800 246 1357</span>
      <span class="call-sub">To find out how you can earn more now!</span>
    </div>

    <div class="promo-photo" role="img" aria-label="Photo of a smiling young man on a sofa with a laptop">
      <p class="promo-link"><a href="#">Click here</a> to find out<br>why you should try this</p>
    </div>

    <div class="register"><a href="#">Register here</a> to help us help you start your new, easier life!</div>

    <div class="video-panel">
      <p class="video-label">Watch our 60 second clip:</p>
      <div class="video-frame" role="img" aria-label="Video still of a happy family lying on grass">
        <svg width="80" height="80" viewBox="0 0 80 80" aria-hidden="true">
          <circle cx="40" cy="40" r="40" fill="#ffffff" fill-opacity=".75"/>
          <path d="M31 22 L58 40 L31 58 Z" fill="#555"/>
        </svg>
      </div>
    </div>

    <h2 class="section-title" style="left:580px;top:690px">Sed suscipit purus nulla, eget dictum libero.</h2>
    <div class="copy" style="left:580px;top:732px;width:470px">
      <p>Proin quis nisl libero. Vivamus egestas tempus elit, at placerat urna convallis nec. Sed malesuada, leo vitae tristique aliquam, mauris massa vehicula tortor, in ullamcorper purus mi vitae magna. Nullam sit amet luctusneque. Vestibulum vel elit nec justo hendrerit imperdiet. Suspendisse eget lorem eget leo iaculis feugiat. Ut non est est. Mauris vitae mi ut diam tempor aliquet.</p>
    </div>

    <div class="quote-box">
      <q>"I wish I had started sooner!"</q>
      <a href="#">Read our members' testimonials...</a>
    </div>
    <div class="family-photo" role="img" aria-label="Photo of a smiling mother and young daughter"></div>
  </main>

  <footer>
    <nav class="site-footer">
      <a href="#">Sitemap</a><a href="#">Privacy policy</a><a href="#">Terms &amp; Conditions</a><a href="#">Contact us</a>
    </nav>
    <p class="copyright">Copyright 2009</p>
  </footer>
</div>
</body>
</html>
```